Text heavy poster for university audience

I have developed a set of standards for online teaching that need to be turned into a post format. The project has a logo which should be incorporated. Most of the designing will be in terms of text layout. The logo (two versions - higher quality files available) and the a sample of standards (as image - word version available; the example is one third of standards) are attached. Design that can be adapted to brochure format would be great. (Brochure adaption will be paid separately via another project to be opened here). More details available here: http://www.brightmeadowhub.org
Updates

Dear all,

The URL for the site needs to be include in the design - either as footer or under logo:
<http://www.brightmeadowhub.org>

Sorry for late notice

Target Market(s)

The are university staff

Industry/Entity Type

University

Font styles to use
Serif
Sans Serif

Requirements
Must have
• The text in the "required" attachment must be included; but for initial draft feel free to restrict your design to "sample" attachment
The green from the Logo (PANTONE 17-5641 Emerald) should be the foundation of the colour palette.
Nice to have
• The collaborators as named here: http://www.brightmeadowhub.org/collaborators/
My preferred find is helvetica neue, but similar can be used
Should not have
• Decorative fonts

```html
<!DOCTYPE html>
<html lang="en">
<head>
<meta charset="utf-8">
<title>Standards Online Education</title>
<link rel="stylesheet" href="https://fonts.googleapis.com/css2?family=Arimo:wght@400;700&family=Tinos&display=swap">
<style>
:root{
  --emerald:#1f9a74;
  --ink:#ffffff;
  --rule:rgba(255,255,255,.55);
  --sans:"Arimo",Arial,sans-serif;
  --serif:"Tinos","Times New Roman",serif;
}
*{margin:0;padding:0;box-sizing:border-box}
html,body{width:846px;height:1200px;overflow:hidden;background:var(--emerald)}
.poster{position:relative;width:846px;height:1200px;background:var(--emerald);color:var(--ink);font-family:var(--serif)}
.title{position:absolute;left:26px;top:12px;font-family:var(--sans);font-weight:700;font-size:86px;line-height:76px;letter-spacing:-2.5px}
.double-rule{position:absolute;left:28px;right:28px;height:9px;border-top:3px solid var(--ink);border-bottom:3px solid var(--ink)}
.double-rule.top{top:270px}
.double-rule.bottom{top:1114px;height:7px;border-top-width:2px;border-bottom-width:2px}
.col-divider{position:absolute;top:292px;height:815px;width:1px;background:var(--rule)}

.column{position:absolute;top:312px}
.col-students{left:28px;width:254px}
.col-middle{left:294px;width:248px;top:324px}
.col-org{left:566px;width:254px;top:325px}

.standard{font-size:10.5px;line-height:13px;margin-bottom:14px}
.standard p{margin:0}
.section-title{font-family:var(--sans);font-weight:700;font-size:33px;letter-spacing:-1.2px;line-height:36px;margin-bottom:4px}
.section-intro{font-family:var(--sans);font-weight:700;font-size:11.5px;line-height:14px;letter-spacing:-.2px;margin-bottom:26px}
.section-intro.small{font-size:7.5px;line-height:10px;letter-spacing:0;margin-bottom:12px}
.standard-title{font-family:var(--sans);font-weight:700;font-size:9.5px;line-height:12.5px;letter-spacing:-.1px;margin-bottom:4px}
.label,.excellent{font-family:var(--sans);font-weight:700}
.standard.small{font-size:7.5px;line-height:9.6px;margin-bottom:10px}
.standard.small .standard-title{margin-bottom:3px}
.standard.small .label,.standard.small .excellent{font-family:var(--serif);font-weight:400}
.standard.org-lead{font-family:var(--sans);font-weight:700;font-size:7.5px;line-height:10px}
.standard.org-lead .label,.standard.org-lead .excellent{font-weight:700}

.col-org .standard{font-size:10.5px;line-height:13px;margin-bottom:12px}
.col-org .standard-title{font-family:var(--serif);font-weight:400;font-size:10.5px;line-height:13px;letter-spacing:0;margin-bottom:0}
.col-org .label,.col-org .excellent{font-family:var(--serif);font-weight:400}
.col-org .gap{height:40px}

.license-mark{position:absolute;left:566px;top:898px;display:flex;align-items:center;gap:6px;font-family:var(--sans);font-weight:700;font-size:16px}
.license-mark .dot{width:18px;height:18px;border:2px solid var(--ink);border-radius:50%}
.license{position:absolute;left:566px;width:252px;font-family:var(--sans);font-size:8px;line-height:10.5px}
.footer-brand{position:absolute;left:30px;top:1132px;display:flex;align-items:center;gap:8px;font-family:var(--sans);font-weight:700;font-size:11px;line-height:12px}
.footer-brand .square{width:30px;height:30px;background:var(--ink)}
.credit{position:absolute;right:26px;top:1134px;font-family:var(--sans);font-weight:700;font-size:17px;text-align:right}
.site-url{position:absolute;right:26px;top:1160px;font-family:var(--sans);font-size:9px;text-align:right}
</style>
</head>
<body>
<main class="poster">
  <h1 class="title">Standards<br>Online<br>Education</h1>
  <div class="double-rule top"></div>
  <div class="col-divider" style="left:283px"></div>
  <div class="col-divider" style="left:548px"></div>

  <div class="column col-students">
    <h2 class="section-title">I. Students</h2>
    <p class="section-intro">Students are supported in their online learning with a quality curriculum [1-4], opportunities for interaction with peers and staff [5&amp;6], and appropriate support [7&amp;8].</p>

    <section class="standard">
      <h3 class="standard-title">1. Curriculum materials are aligned, available and engaging</h3>
      <p><span class="label">Threshold-</span> The necessary materials are constructively aligned and available online</p>
      <p><span class="label">Good-</span> The materials are provided using a variety of media to engage students and support diversity</p>
      <p class="excellent">Excellent</p>
    </section>
    <section class="standard">
      <h3 class="standard-title">2. Learning activities are aligned, available and engaging</h3>
      <p><span class="label">Threshold-</span> Constructively aligned learning activities are available online</p>
      <p><span class="label">Good-</span> Learning activities use a variety of appropriate technologies to engage students and support diversity</p>
      <p class="excellent">Excellent</p>
    </section>
    <section class="standard">
      <h3 class="standard-title">3. Assessment tasks are aligned, available and engaging</h3>
      <p><span class="label">Threshold-</span>Constructively aligned assessment tasks are available online</p>
      <p><span class="label">Good-</span>Assessment tasks use a variety of appropriate technologies to engage students and support diversity</p>
      <p class="excellent">Excellent</p>
    </section>
    <section class="standard">
      <h3 class="standard-title">4. Students are provided with timely, improvement focused formative feedback</h3>
      <p><span class="label">Threshold-</span>Appropriate technologies are used to provide students with formative feedback in a timely manner</p>
      <p><span class="label">Good</span>&emsp;Feedback is provided in a variety of media to engage students and support diversity</p>
      <p class="excellent">Excellent</p>
    </section>
    <section class="standard">
      <h3 class="standard-title">5. Students are provided with opportunities to interact with peers</h3>
      <p><span class="label">Threshold</span> There are opportunities for social interaction</p>
      <p><span class="label">Good</span>&emsp;There are opportunities for learning-focused interaction</p>
      <p class="excellent">Excellent</p>
    </section>
    <section class="standard">
      <h3 class="standard-title">6. Students are provided with opportunities to interact with staff</h3>
      <p><span class="label">Threshold</span> Staff are provided with opportunities to answer student queries</p>
      <p><span class="label">Good</span>&emsp;Staff are provided with opportunities to be active participants in learning-focused interactions</p>
      <p class="excellent">Excellent</p>
    </section>
  </div>

  <div class="column col-middle">
    <section class="standard">
      <h3 class="standard-title">7. Students are provided with appropriate learning support</h3>
      <p><span class="label">Threshold</span> Appropriate, up-to-date and reliable learning guides and resources are provided online</p>
      <p><span class="label">Good</span>&emsp;A range of appropriate, up-to-date and reliable online learning skills workshops are available</p>
      <p class="excellent">Excellent</p>
    </section>
    <section class="standard" style="margin-bottom:26px">
      <h3 class="standard-title">8. Students are supported in their use of educational technology</h3>
      <p><span class="label">Threshold</span> Appropriate, up-to-date and reliable technological guides and resources are provided online</p>
      <p><span class="label">Good</span>&emsp;Appropriate, timely and reliable asynchronous technological support is available</p>
      <p class="excellent">Excellent</p>
    </section>

    <h2 class="section-title">II. Staff</h2>
    <p class="section-intro small">Staff are supported in their online teaching with quality professional development [9], resourcing [10] and technical support [11].</p>
    <section class="standard small">
      <h3 class="standard-title">9. Staff are provided with quality professional development in online education</h3>
      <p><span class="label">Threshold</span>&emsp;A range of appropriate, up-to-date and informative professional development activities are available to staff</p>
      <p><span class="label">Good</span>&ensp;The organisation requires staff to engage in continued professional development relevant to online education</p>
      <p class="excellent">Excellent</p>
    </section>
    <section class="standard small">
      <h3 class="standard-title">10. Online education is recognised in workload</h3>
      <p><span class="label">Threshold</span>&emsp;Online teaching is recognised in workload</p>
      <p><span class="label">Good</span>&ensp;Online unit development is recognised in workload</p>
      <p class="excellent">Excellent</p>
    </section>
    <section class="standard small" style="margin-bottom:24px">
      <h3 class="standard-title">11. Staff are supported in their use of educational technology</h3>
      <p><span class="label">Threshold</span>&emsp;Appropriate, up-to-date and reliable technological guides and resources are provided online</p>
      <p><span class="label">Good</span>&ensp;Appropriate, timely and reliable asynchronous technological support is available</p>
      <p class="excellent">Excellent</p>
    </section>

    <h2 class="section-title">III. Organization</h2>
    <p class="section-intro small" style="margin-top:14px">The organisation supports online education through the provision of quality leadership [12-13], infrastructure [14] and evaluation [15-17]</p>
    <section class="standard org-lead">
      <p>12. The organisation provides strategic leadership in online education</p>
      <p><span class="label">Threshold</span>&emsp;The organisation has a clearly articulated strategic position on online education</p>
      <p><span class="label">Good</span> An appropriate member of the executive has explicit responsibility for online education</p>
      <p class="excellent">Excellent</p>
    </section>
  </div>

  <div class="column col-org">
    <section class="standard">
      <h3 class="standard-title">13. The organisation employs a systematic approach to resource allocation in online education</h3>
      <p><span class="label">Threshold</span>&emsp;There is a systematic approach to resource allocation</p>
      <p><span class="label">Good</span>There is systematic approach with formal criteria that are widely available</p>
      <p class="excellent">Excellent</p>
    </section>
    <section class="standard">
      <h3 class="standard-title">14. The organisation maintains and supports a quality learning platform for delivering online education</h3>
      <p><span class="label">Threshold</span>&emsp;The organisation maintains and supports an appropriate learning platform</p>
      <p><span class="label">Good</span>The learning platform provided is fit for purpose, scalable and reliable</p>
      <p class="excellent">Excellent</p>
    </section>
    <div class="gap"></div>
    <section class="standard">
      <h3 class="standard-title">15. The organisation has a process for evaluating and improving student satisfaction with online education</h3>
      <p><span class="label">Threshold</span>&emsp;The organisation has a systematic process for evaluating and improving student satisfaction with online education</p>
      <p><span class="label">Good</span>The organisation has a systematic process for improving student learning outcomes and satisfaction with online education and communicating improvements to students</p>
      <p class="excellent">Excellent</p>
    </section>
    <section class="standard">
      <h3 class="standard-title">16. The organisation has a process for evaluating and improving training and support for staff</h3>
      <p><span class="label">Threshold</span>&emsp;The organisation has a systematic process for evaluating and improving staff training and support</p>
      <p><span class="label">Good</span>The organisation has a systematic process for improving staff training and support and communicating improvements to staff</p>
      <p class="excellent">Excellent</p>
    </section>
  </div>

  <div class="license-mark"><span class="dot"></span>Open Share Commons</div>
  <p class="license" style="top:930px">This work is licensed under the Open Share Commons Attribution-ShareAlike 3.0 Unported License. To view a copy of this license, visit http://www.opensharecommons.org/licenses/by-sa/3.0/ or send a letter to Open Share Commons, 210 Alder Lane, Suite 400, Fernvale, California, 90112, USA.</p>
  <p class="license" style="top:1005px">Support for this activity has been provided by the National Office for Teaching Quality. The views expressed in this activity do not necessarily reflect the views of the National Office for Teaching Quality.</p>

  <div class="double-rule bottom"></div>
  <div class="footer-brand"><span class="square"></span><span>BRIGHTMEADOW<br>HUB</span></div>
  <p class="credit">Dana Whitlock and Collaborators</p>
  <p class="site-url">http://www.brightmeadowhub.org</p>
</main>
</body>
</html>
```